iPhone iOS 7 App For Managing Tasks/Photos for Internal Company Use

We need an app design that displays company objectives and task, and provides the interface for employees to complete a task by uploading a photo and adding comments.

Please see attached mock up sketches as a rough guideline

Final delivery of files must contain PSD, and all layers/objects sliced both is PSD and PNG files

Target Market(s)

This is a tool for internal employee use

Industry/Entity Type

It Company

Requirements
Must have
• Must include logo, and match the colour scheme
Use iPhone iOS 7 Style

```html
<!DOCTYPE html>
<html lang="en">
<head>
<meta charset="utf-8">
<title>Objective #1 – Task List</title>
<link rel="stylesheet" href="https://fonts.googleapis.com/css2?family=Open+Sans:wght@400;600;700;800&display=swap">
<style>
  :root {
    --status-top: #f2f2f2;
    --status-bottom: #c9c9c9;
    --header-top: #3a5fa8;
    --header-bottom: #142f6e;
    --row-top: #f7f7f7;
    --row-bottom: #e6e6e6;
    --row-line: #c8c8c8;
    --rail: #26364c;
    --rail-edge: #3b4d66;
    --icon-blue: #3fb3ee;
    --title: #3a3a3a;
    --meta: #8a8a8a;
    --time: #2a98d6;
    --tick-active: #2a98d6;
    --tick: #4a4a4a;
    --tabbar: #121b27;
    --tab-label: #ffffff;
    --touch: rgba(240, 110, 110, 0.35);
  }
  * { box-sizing: border-box; margin: 0; padding: 0; }
  html, body { width: 800px; height: 1200px; overflow: hidden; }
  body { font-family: "Open Sans", Arial, sans-serif; background: #ffffff; }

  .screen { width: 800px; height: 1200px; display: flex; flex-direction: column; position: relative; }

  .status-bar {
    height: 50px;
    background: linear-gradient(var(--status-top), var(--status-bottom));
    display: flex; align-items: center; justify-content: space-between;
    padding: 0 12px;
    position: relative;
  }
  .status-time {
    position: absolute; left: 0; right: 0; text-align: center;
    font-size: 31px; font-weight: 600; color: #111;
  }

  .nav-header {
    height: 112px;
    background: linear-gradient(var(--header-top), var(--header-bottom));
    border-bottom: 2px solid #0c1f4a;
    display: flex; align-items: center; justify-content: center;
  }
  .nav-title { color: #ffffff; font-size: 44px; font-weight: 700; letter-spacing: 0.5px; }

  .task-list { list-style: none; flex: 1; overflow: hidden; }
  .task-row {
    height: 147.5px;
    display: flex; align-items: center;
    background: linear-gradient(var(--row-top), var(--row-bottom));
    border-bottom: 2px solid var(--row-line);
    position: relative;
  }
  .task-rail {
    width: 130px; height: 100%;
    background: var(--rail);
    border-right: 3px solid var(--rail-edge);
    border-bottom: 2px solid #1a2637;
    display: flex; align-items: center; justify-content: center;
    flex-shrink: 0;
  }
  .task-body { flex: 1; padding-left: 37px; }
  .task-title { font-size: 33px; font-weight: 700; color: var(--title); line-height: 1.2; }
  .task-category { font-size: 25px; font-weight: 600; color: var(--meta); margin-top: 14px; }
  .task-time {
    width: 150px; font-size: 25px; font-weight: 400; color: var(--time);
    text-align: left; position: relative;
  }
  .touch-mark {
    position: absolute; left: 52px; top: -28px;
    width: 72px; height: 72px; border-radius: 50%;
    background: var(--touch);
  }
  .task-time span { position: relative; }
  .task-check { width: 72px; display: flex; justify-content: flex-start; }

  .tab-bar {
    height: 155px;
    background: linear-gradient(#1c2736, var(--tabbar));
    display: flex; justify-content: space-around; align-items: center;
    position: absolute; left: 0; right: 0; bottom: 0;
  }
  .tab { width: 200px; display: flex; flex-direction: column; align-items: center; }
  .tab-icon { width: 92px; height: 92px; }
  .tab-label { color: var(--tab-label); font-size: 27px; font-weight: 700; margin-top: 6px; }
</style>
</head>
<body>
<div class="screen">
  <div class="status-bar">
    <svg width="70" height="30" viewBox="0 0 70 30" aria-label="Signal">
      <rect x="2" y="20" width="9" height="8" fill="#222"/>
      <rect x="15" y="15" width="9" height="13" fill="#222"/>
      <rect x="28" y="10" width="9" height="18" fill="#222"/>
      <rect x="41" y="5" width="9" height="23" fill="#222"/>
      <rect x="54" y="0" width="9" height="28" fill="#222"/>
    </svg>
    <div class="status-time">9:20 AM</div>
    <svg width="60" height="28" viewBox="0 0 60 28" aria-label="Battery">
      <rect x="1" y="2" width="52" height="24" rx="4" fill="none" stroke="#222" stroke-width="2"/>
      <rect x="5" y="6" width="44" height="16" rx="2" fill="#222"/>
      <rect x="54" y="9" width="5" height="10" rx="1" fill="#222"/>
    </svg>
  </div>

  <header class="nav-header"><h1 class="nav-title">Objective #1</h1></header>

  <ul class="task-list">
    <li class="task-row">
      <div class="task-rail"><svg class="edit-icon" width="56" height="56" viewBox="0 0 56 56"><rect x="4" y="8" width="44" height="44" rx="5" fill="none" stroke="var(--icon-blue)" stroke-width="6"/><path d="M22 36 L24 28 L46 6 L52 12 L30 34 Z" fill="var(--icon-blue)" stroke="var(--rail)" stroke-width="3"/></svg></div>
      <div class="task-body"><div class="task-title">List of Latin phrases</div><div class="task-category">Personal</div></div>
      <div class="task-time"><span>9.00 AM</span></div>
      <div class="task-check"><svg width="34" height="28" viewBox="0 0 34 28"><path d="M3 15 L12 24 L31 4" fill="none" stroke="var(--tick-active)" stroke-width="5"/></svg></div>
    </li>
    <li class="task-row">
      <div class="task-rail"><svg width="56" height="56" viewBox="0 0 56 56"><rect x="4" y="8" width="44" height="44" rx="5" fill="none" stroke="var(--icon-blue)" stroke-width="6"/><path d="M22 36 L24 28 L46 6 L52 12 L30 34 Z" fill="var(--icon-blue)" stroke="var(--rail)" stroke-width="3"/></svg></div>
      <div class="task-body"><div class="task-title">Metasyntactic variable</div><div class="task-category">Work</div></div>
      <div class="task-time"><div class="touch-mark"></div><span>9.00 AM</span></div>
      <div class="task-check"><svg width="34" height="28" viewBox="0 0 34 28"><path d="M3 15 L12 24 L31 4" fill="none" stroke="var(--tick)" stroke-width="5"/></svg></div>
    </li>
    <li class="task-row">
      <div class="task-rail"><svg width="56" height="56" viewBox="0 0 56 56"><rect x="4" y="8" width="44" height="44" rx="5" fill="none" stroke="var(--icon-blue)" stroke-width="6"/><path d="M22 36 L24 28 L46 6 L52 12 L30 34 Z" fill="var(--icon-blue)" stroke="var(--rail)" stroke-width="3"/></svg></div>
      <div class="task-body"><div class="task-title">Asemic writing</div><div class="task-category">Personal</div></div>
      <div class="task-time"><span>9.00 AM</span></div>
      <div class="task-check"><svg width="34" height="28" viewBox="0 0 34 28"><path d="M3 15 L12 24 L31 4" fill="none" stroke="var(--tick)" stroke-width="5"/></svg></div>
    </li>
    <li class="task-row">
      <div class="task-rail"><svg width="56" height="56" viewBox="0 0 56 56"><rect x="4" y="8" width="44" height="44" rx="5" fill="none" stroke="var(--icon-blue)" stroke-width="6"/><path d="M22 36 L24 28 L46 6 L52 12 L30 34 Z" fill="var(--icon-blue)" stroke="var(--rail)" stroke-width="3"/></svg></div>
      <div class="task-body"><div class="task-title">Etaoin shrdlu</div><div class="task-category">Work</div></div>
      <div class="task-time"><span>9.00 AM</span></div>
      <div class="task-check"><svg width="34" height="28" viewBox="0 0 34 28"><path d="M3 15 L12 24 L31 4" fill="none" stroke="var(--tick)" stroke-width="5"/></svg></div>
    </li>
    <li class="task-row">
      <div class="task-rail"><svg width="56" height="56" viewBox="0 0 56 56"><rect x="4" y="8" width="44" height="44" rx="5" fill="none" stroke="var(--icon-blue)" stroke-width="6"/><path d="M22 36 L24 28 L46 6 L52 12 L30 34 Z" fill="var(--icon-blue)" stroke="var(--rail)" stroke-width="3"/></svg></div>
      <div class="task-body"><div class="task-title">Filler text</div><div class="task-category">Personal</div></div>
      <div class="task-time"><span>9.00 AM</span></div>
      <div class="task-check"><svg width="34" height="28" viewBox="0 0 34 28"><path d="M3 15 L12 24 L31 4" fill="none" stroke="var(--tick)" stroke-width="5"/></svg></div>
    </li>
    <li class="task-row">
      <div class="task-rail"><svg width="56" height="56" viewBox="0 0 56 56"><rect x="4" y="8" width="44" height="44" rx="5" fill="none" stroke="var(--icon-blue)" stroke-width="6"/><path d="M22 36 L24 28 L46 6 L52 12 L30 34 Z" fill="var(--icon-blue)" stroke="var(--rail)" stroke-width="3"/></svg></div>
      <div class="task-body"><div class="task-title">Filler text</div><div class="task-category">Personal</div></div>
      <div class="task-time"><span>9.00 AM</span></div>
      <div class="task-check"><svg width="34" height="28" viewBox="0 0 34 28"><path d="M3 15 L12 24 L31 4" fill="none" stroke="var(--tick)" stroke-width="5"/></svg></div>
    </li>
  </ul>

  <nav class="tab-bar">
    <div class="tab">
      <svg class="tab-icon" viewBox="0 0 92 92" aria-label="Home">
        <defs><linearGradient id="home-bg" x1="0" y1="0" x2="0" y2="1"><stop offset="0" stop-color="#ffa23a"/><stop offset="1" stop-color="#e0600a"/></linearGradient></defs>
        <rect x="4" y="4" width="84" height="84" rx="14" fill="url(#home-bg)"/>
        <path d="M46 20 L72 44 L64 44 L64 70 L52 70 L52 54 L40 54 L40 70 L28 70 L28 44 L20 44 Z" fill="#ffffff"/>
      </svg>
      <span class="tab-label">Home</span>
    </div>
    <div class="tab">
      <svg class="tab-icon" viewBox="0 0 92 92" aria-label="Objective">
        <rect x="4" y="4" width="84" height="84" rx="14" fill="#3a2a22"/>
        <circle cx="46" cy="48" r="32" fill="#c91c1c"/>
        <circle cx="46" cy="48" r="24" fill="#f2f2f2"/>
        <circle cx="46" cy="48" r="16" fill="#c91c1c"/>
        <circle cx="46" cy="48" r="8" fill="#f2f2f2"/>
        <path d="M46 48 L74 18" stroke="#d8b25a" stroke-width="4"/>
      </svg>
      <span class="tab-label">Objective</span>
    </div>
    <div class="tab">
      <svg class="tab-icon" viewBox="0 0 92 92" aria-label="News">
        <rect x="4" y="4" width="84" height="84" rx="14" fill="#0d1a4a" stroke="#8ea0c8" stroke-width="3"/>
        <circle cx="46" cy="38" r="22" fill="#2b7fd4"/>
        <ellipse cx="46" cy="38" rx="10" ry="22" fill="none" stroke="#bfe0ff" stroke-width="2"/>
        <path d="M24 38 H68 M28 27 H64 M28 49 H64" stroke="#bfe0ff" stroke-width="2"/>
        <rect x="22" y="64" width="48" height="16" rx="3" fill="#1f5fb0"/>
        <text x="46" y="76.5" text-anchor="middle" font-family="Open Sans, Arial, sans-serif" font-size="12" font-weight="700" fill="#ffffff">News</text>
      </svg>
      <span class="tab-label">News</span>
    </div>
    <div class="tab">
      <svg class="tab-icon" viewBox="0 0 92 92" aria-label="Logout">
        <defs><linearGradient id="logout-bg" x1="0" y1="0" x2="0" y2="1"><stop offset="0" stop-color="#ff4a4a"/><stop offset="1" stop-color="#b80d0d"/></linearGradient></defs>
        <rect x="4" y="4" width="84" height="84" rx="14" fill="url(#logout-bg)"/>
        <path d="M34 30 A22 22 0 1 0 58 30" fill="none" stroke="#ffffff" stroke-width="7" stroke-linecap="round"/>
        <path d="M46 20 V48" stroke="#ffffff" stroke-width="7" stroke-linecap="round"/>
      </svg>
      <span class="tab-label">Logout</span>
    </div>
  </nav>
</div>
</body>
</html>
```